theater production in Seoul needs a poster of "Courtship Tutor: The Revue"

Title: "Courtship Tutor: The Revue"
Concept: This is a lively and fun musical centered around a dating coach who helps people navigate the ups and downs of modern romance. The show is full of humor, love, and the occasional heartache, highlighting the challenges of finding true love in today's world.
Visual Style: We are aiming for a vibrant and eye-catching design that captures the playful and romantic mood of the show. Think of bright colors, romantic symbols like hearts or arrows, and a modern urban setting. It should feel inviting, slightly humorous, and engaging.
Target Audience: Young adults and adults who enjoy romantic comedies and upbeat musicals. The tone should be fun and light, with a hint of romance.
Key Imagery: Possible elements could include a charismatic coach character holding a notepad or a whistle, silhouettes of couples, a city skyline in the background, or playful icons like phones, roses, and hearts. We want the poster to convey a sense of romance, excitement, and fun.

Text Elements:

Catchy tagline: "Finding love, one date at a time!"

Performance dates:2025. March 15_ May 31th
Sat. 1PM, Sun. 3pm, Wed/Fri 7:30pm

where:Hwasolgil Arthall
TICKET PRICE: $45
on the bottom side
Author Pyo Dain
Director-Gil Sorahm Composer_Moonbitnari
Producer_Ryu Donghwan Sound Director _Ahn Wol
actor_Tak Minjae Jeon Hyerin Nam Jiwoon Ha Boram Yeo Sanghun Cha Dohyeon

BOOK NOW
02 418-3956
PLUM COMPANY

```html
<!DOCTYPE html>
<html lang="en">
<head>
<meta charset="utf-8">
<title>Courtship Tutor: The Revue</title>
<link href="https://fonts.googleapis.com/css2?family=Bebas+Neue&family=Poppins:wght@300;400;500;600;700;800;900&family=Allura&family=Yellowtail&display=swap" rel="stylesheet">
<style>
  :root {
    --red-top: #8a0303;
    --red-mid: #6d0202;
    --red-deep: #420505;
    --yellow: #ffc800;
    --white: #ffffff;
    --ink: #111111;
    --badge-red: #d8200c;
    --gold-bar: #c8950a;
    --red-bar: #b51212;
    --grey-bar: #a89090;
    --coach-blue: #1d3f78;
    --silhouette: #d10f0f;
  }
  * { margin: 0; padding: 0; box-sizing: border-box; }
  html, body { width: 890px; height: 1200px; overflow: hidden; background: #b3b3b3; }
  .poster {
    position: relative; width: 890px; height: 1200px; overflow: hidden;
    background: linear-gradient(180deg, var(--red-top) 0%, var(--red-mid) 55%, var(--red-deep) 100%);
    font-family: "Poppins", sans-serif; color: var(--white);
  }
  .abs { position: absolute; }
  .skyline-glow {
    left: 0; top: 300px; width: 890px; height: 600px;
    background: radial-gradient(ellipse at 40% 50%, rgba(200,20,20,0.35), rgba(0,0,0,0) 70%);
  }
  .couple-silhouette {
    left: 600px; top: 140px; width: 240px; height: 310px;
    background: radial-gradient(ellipse at 50% 45%, var(--silhouette), rgba(209,15,15,0) 72%);
  }
  .coach-figure {
    left: 440px; top: 290px; width: 430px; height: 850px;
    background: linear-gradient(180deg, rgba(29,63,120,0.0) 0%, rgba(29,63,120,0.85) 30%, var(--coach-blue) 80%, rgba(29,63,120,0.0) 100%);
    border-radius: 180px 180px 40px 40px;
  }
  .title { left: 59px; top: 52px; font-family: "Bebas Neue", sans-serif; line-height: 0.86; font-size: 96px; letter-spacing: 1px; }
  .title-line-white { color: var(--white); }
  .title-line-yellow { color: var(--yellow); }
  .title-script { left: 66px; top: 268px; font-family: "Allura", cursive; font-size: 78px; color: var(--white); transform: rotate(-4deg); }
  .tagline-spaced { left: 60px; top: 402px; font-size: 25px; font-weight: 400; letter-spacing: 12px; line-height: 1.2; }
  .tagline-bold { left: 60px; top: 462px; font-family: "Bebas Neue", sans-serif; font-size: 84px; line-height: 0.9; }
  .tagline-script { left: 60px; top: 518px; font-family: "Allura", cursive; font-size: 64px; color: var(--ink); }
  .tagline-time { left: 60px; top: 588px; font-weight: 900; font-size: 72px; line-height: 1; }
  .venue-bar { left: 60px; top: 679px; width: 406px; height: 37px; display: flex; background: var(--ink); }
  .venue-label { width: 81px; border-right: 2px solid #7a0000; display: flex; align-items: center; justify-content: center; font-size: 13px; letter-spacing: 2px; font-weight: 300; }
  .venue-name { flex: 1; display: flex; align-items: center; padding-left: 14px; font-size: 18px; font-weight: 700; letter-spacing: 3px; }
  .ticket-label { left: 60px; top: 758px; font-size: 17px; letter-spacing: 3px; font-weight: 300; }
  .ticket-price { left: 60px; top: 776px; font-weight: 800; font-size: 84px; line-height: 1.1; letter-spacing: -2px; }
  .ticket-price sup { font-size: 44px; vertical-align: 28px; }
  .divider { left: 254px; top: 766px; height: 106px; border-left: 1px dashed rgba(255,255,255,0.7); }
  .author-label { left: 291px; top: 760px; font-size: 22px; letter-spacing: 6px; font-weight: 400; }
  .author-name { left: 291px; top: 794px; font-family: "Yellowtail", cursive; font-size: 50px; color: var(--yellow); }
  .credit { font-size: 11.5px; line-height: 1.3; }
  .credit-role { color: var(--yellow); letter-spacing: 4px; font-size: 11px; font-weight: 500; }
  .company { left: 48px; top: 1052px; font-family: "Bebas Neue", sans-serif; font-size: 46px; line-height: 0.93; }
  .book-now { left: 290px; top: 1028px; font-family: "Allura", cursive; font-size: 62px; color: var(--badge-red); transform: rotate(-5deg); }
  .book-now span { color: var(--white); }
  .phone { left: 250px; top: 1100px; display: flex; align-items: center; gap: 10px; font-weight: 800; font-size: 34px; }
  .dates-box { left: 689px; top: 584px; width: 145px; height: 307px; border: 2px solid var(--badge-red); text-align: center; background: rgba(90,0,0,0.35); }
  .dates-head { background: var(--badge-red); height: 33px; font-size: 11.5px; line-height: 1.15; padding-top: 3px; }
  .dates-month { font-weight: 600; font-size: 34px; line-height: 1; margin-top: 4px; }
  .dates-day { font-weight: 800; font-size: 66px; line-height: 0.9; }
  .dates-to { font-family: "Yellowtail", cursive; color: var(--yellow); font-size: 28px; line-height: 0.8; }
  .dates-year { font-size: 21px; letter-spacing: 3px; font-weight: 500; line-height: 1.1; }
  .time-bar { left: 689px; width: 145px; height: 24px; font-size: 13px; padding-left: 12px; display: flex; align-items: center; color: var(--ink); }
  .time-bar b { font-weight: 700; margin-left: 3px; }
  .time-sat { top: 892px; background: var(--gold-bar); }
  .time-sun { top: 918px; background: var(--red-bar); color: var(--white); }
  .time-wed { top: 944px; background: var(--grey-bar); }
</style>
</head>
<body>
<div class="poster">
  <div class="abs skyline-glow" role="img" aria-label="Faint red city skyline with floating hearts"></div>
  <div class="abs couple-silhouette" role="img" aria-label="Red silhouette of a couple embracing"></div>
  <div class="abs coach-figure" role="img" aria-label="Illustrated dating coach in a blue suit holding a paper and a pen"></div>

  <h1 class="abs title">
    <span class="title-line-white">COURTSHIP</span><br>
    <span class="title-line-yellow">TUTOR</span>
  </h1>
  <div class="abs title-script">The Revue</div>

  <div class="abs tagline-spaced">FINDING<br>LOVE</div>
  <div class="abs tagline-bold">ONE DATE</div>
  <div class="abs tagline-script">at a</div>
  <div class="abs tagline-time">TIME!</div>

  <div class="abs venue-bar">
    <div class="venue-label">VENUE</div>
    <div class="venue-name">HWASOLGIL ARTHALL</div>
  </div>

  <div class="abs ticket-label">TICKET PRICE</div>
  <div class="abs ticket-price"><sup>$</sup>45</div>
  <div class="abs divider"></div>
  <div class="abs author-label">AUTHOR</div>
  <div class="abs author-name">Pyo Dain</div>

  <div class="abs credit" style="left:59px;top:904px"><div class="credit-role">DIRECTOR</div>Gil Sorahm</div>
  <div class="abs credit" style="left:59px;top:951px"><div class="credit-role">COMPOSER</div>Moonbitnari</div>
  <div class="abs credit" style="left:202px;top:904px"><div class="credit-role">PRODUCER</div>Ryu Donghwan</div>
  <div class="abs credit" style="left:202px;top:951px"><div class="credit-role">SOUND<br>DIRECTOR</div>Ahn Wol</div>
  <div class="abs credit" style="left:350px;top:905px"><div class="credit-role">ACTOR</div>Tak Minjae<br>Jeon Hyerin<br>Nam Jiwoon<br>Ha Boram<br>Yeo Sanghun<br>Cha Dohyeon</div>

  <div class="abs company">PLUM<br>COMPANY</div>
  <div class="abs book-now">Book <span>Now!</span></div>
  <div class="abs phone">
    <svg width="20" height="20" viewBox="0 0 20 20" aria-hidden="true">
      <circle cx="10" cy="10" r="10" fill="#d8200c"/>
      <path d="M6.5 5.5c.6-.6 1.3-.4 1.6.2l.8 1.6c.2.5 0 1-.4 1.3l-.6.4c.5 1.2 1.4 2.1 2.6 2.6l.4-.6c.3-.4.8-.6 1.3-.4l1.6.8c.6.3.8 1 .2 1.6-.9.9-2.2 1.1-3.4.5-2-1-3.6-2.6-4.6-4.6-.6-1.2-.4-2.5.5-3.4z" fill="#fff"/>
    </svg>
    02 418-3956
  </div>

  <div class="abs dates-box">
    <div class="dates-head">PERFORMANCE<br>DATES</div>
    <div class="dates-month">MAR</div>
    <div class="dates-day">15</div>
    <div class="dates-to">to</div>
    <div class="dates-month" style="margin-top:0">MAY</div>
    <div class="dates-day">31</div>
    <div class="dates-year">2025</div>
  </div>
  <div class="abs time-bar time-sat">Sat: <b>1.00pm</b></div>
  <div class="abs time-bar time-sun">Sun: <b>3.00pm</b></div>
  <div class="abs time-bar time-wed">Wed/Fri: <b>7:30pm</b></div>
</div>
</body>
</html>
```